Estate Planner needs an Ad for a local newsletter

I need an ad designed for my practice as an estate planning attorney. The ad will be in a newsletter that targets individuals over the age of 55. My ad is 7.5"W x 4.6"H (a half page ad) .
The wording should include:
Varnholt, Danielle

Danielle Varnholt

Wisdom Meets Planning
Your Estate, Your Legacy

After 23 years as a military spouse, moving our family of six across the country,
I learned the true value of careful planning. Today I help Palomar County's seniors protect what matters most – their family’s future and their life’s work.

I understand that your estate is more than just assets – it's a lifetime of wise
decisions, cherished memories, and dreams for your family's future.

Professional Estate Planning:
• Wills & Living Trusts • Healthcare Directives
• Power of Attorney • Asset Protection
• Probate Avoidance • Peace of Mind

Plus also needs to have my contact information:
RPV Law
Danielle Varnholt
Attorney/Of Counsel
4712 Cedarbrook Lane
Lakemont, Florida 34999
(555) 684-1093
dvarnholt@rpvlegalteam.example
Logo is attached.

```html
<!DOCTYPE html>
<html lang="en">
<head>
<meta charset="utf-8">
<title>Danielle Varnholt – Estate Planning</title>
<link rel="stylesheet" href="https://fonts.googleapis.com/css2?family=Libre+Baskerville:wght@700&family=Poppins:wght@400;500;600;700&display=swap">
<style>
  :root {
    --brand-blue: #0a4f88;
    --ink: #1c1c1c;
    --paper: #ffffff;
    --photo-dark: #5a5a5a;
    --photo-mid: #9a9a9a;
    --photo-light: #d6d6d6;
    --photo-warm: #b89a78;
  }
  * { margin: 0; padding: 0; box-sizing: border-box; }
  html, body { width: 1200px; height: 736px; overflow: hidden; background: var(--paper); }
  .ad {
    position: relative;
    width: 1200px; height: 736px;
    background: var(--paper);
    font-family: "Poppins", sans-serif;
    color: var(--ink);
    overflow: hidden;
  }
  .brand {
    position: absolute; left: 44px; top: 48px;
    display: flex; align-items: center; gap: 10px;
    font-family: "Poppins", sans-serif; font-weight: 600;
    font-size: 30px; color: var(--brand-blue); line-height: 1;
  }
  .brand-square { width: 14px; height: 14px; background: var(--brand-blue); }
  .attorney-name {
    position: absolute; left: 43px; top: 160px;
    font-family: "Libre Baskerville", serif; font-weight: 700;
    font-size: 58px; line-height: 58px; letter-spacing: -1px;
    color: var(--brand-blue);
  }
  .tagline-band {
    position: absolute; left: 0; top: 286px;
    width: 655px; height: 69px;
    background: var(--brand-blue);
    display: flex; align-items: center; padding-left: 44px;
  }
  .tagline { color: var(--paper); font-size: 22.5px; font-weight: 400; white-space: nowrap; }
  .story {
    position: absolute; left: 44px; top: 391px; width: 560px;
    font-size: 15.5px; line-height: 18.7px; white-space: nowrap;
  }
  .story p + p { margin-top: 18px; }
  .photo { position: absolute; }
  .photo-portrait-man { left: 655px; top: 50px; width: 157px; height: 345px; background: linear-gradient(180deg, var(--photo-light), var(--photo-mid) 55%, var(--photo-dark)); }
  .photo-couple { left: 655px; top: 408px; width: 157px; height: 131px; background: linear-gradient(135deg, #e8e2d8, var(--photo-warm)); }
  .photo-signing { left: 826px; top: 50px; width: 156px; height: 131px; background: linear-gradient(180deg, #e9e9ea, #c79a6c); }
  .photo-portrait-woman { left: 826px; top: 194px; width: 156px; height: 345px; background: linear-gradient(180deg, #8a8a8a, #6a6a6a 50%, #3a3a3a); }
  .photo-portrait-elder { left: 996px; top: 50px; width: 156px; height: 489px; background: linear-gradient(180deg, #cfcfcf, #a8a8a8 60%, #8c8c8c); }
  .footer-band {
    position: absolute; left: 0; top: 581px; width: 1200px; height: 155px;
    background: var(--brand-blue); color: var(--paper);
  }
  .services { position: absolute; left: 43px; top: 26px; }
  .services-title { font-size: 19.5px; font-weight: 700; line-height: 24px; }
  .services-list { list-style: none; font-size: 20px; line-height: 24px; font-weight: 400; }
  .contact {
    position: absolute; right: 48px; top: 23px;
    text-align: right; font-size: 14.5px; line-height: 21.5px; font-weight: 500;
    font-style: normal;
  }
</style>
</head>
<body>
<main class="ad">
  <div class="brand"><span>RPV Law</span><span class="brand-square"></span></div>

  <h1 class="attorney-name">DANIELLE<br>VARNHOLT</h1>

  <div class="tagline-band">
    <p class="tagline">Wisdom Meets Planning! Your Estate, Your Legacy</p>
  </div>

  <section class="story">
    <p>After 23 years as a military spouse, moving our family of six<br>across the country, I learned the true value of careful planning.<br>Today I help Palomar County's seniors protect what matters most<br>– their family’s future and their life’s work.</p>
    <p>I understand that your estate is more than just assets – it's a<br>lifetime of wise decisions, cherished memories, and dreams for<br>your family's future.</p>
  </section>

  <div class="photo photo-portrait-man" role="img" aria-label="Black and white portrait of a smiling older man with white hair and beard"></div>
  <div class="photo photo-couple" role="img" aria-label="Older couple smiling at each other at a table"></div>
  <div class="photo photo-signing" role="img" aria-label="Hand signing a document on a clipboard at a wooden desk"></div>
  <div class="photo photo-portrait-woman" role="img" aria-label="Black and white portrait of an older woman in a tweed jacket"></div>
  <div class="photo photo-portrait-elder" role="img" aria-label="Black and white portrait of a smiling elderly man with glasses and beard"></div>

  <footer class="footer-band">
    <div class="services">
      <h2 class="services-title">Professional Estate Planning:</h2>
      <ul class="services-list">
        <li>• Wills &amp; Living Trusts • Healthcare Directives</li>
        <li>• Power of Attorney • Asset Protection</li>
        <li>• Probate Avoidance • Peace of Mind</li>
      </ul>
    </div>
    <address class="contact">
      Danielle Varnholt<br>
      Attorney/Of Counsel<br>
      4712 Cedarbrook Lane Lakemont, Florida 34999<br>
      (555) 684-1093<br>
      dvarnholt@rpvlegalteam.example
    </address>
  </footer>
</main>
</body>
</html>
```